Create Lanternfield HR Business Cards.

Create Business Cards for Lanternfield HR. 2 sided and Would like the back to have the logo.

Info for Business Card:
Address: 4827 Millbrook Ave Suite 230 Cleveland, Ohio 44987
Office Number: 216-555-0143
Mobile: 216-555-0192

Website: www.lanternfieldhr.example

Target Market(s)

Small to medium size businesses

Industry/Entity Type

Human Resources

Contact Information for Business Card

Company logo and information

Font styles to use
Serif
Sans Serif

Requirements
Must have
• Info for Business Card: Address: 4827 Millbrook Ave Suite 230 Cleveland, Ohio 44987 Office Number: 216-555-0143 Mobile: 216-555-0192 Website: www.lanternfieldhr.example

```html
<!DOCTYPE html>
<html lang="en">
<head>
<meta charset="utf-8">
<title>Lanternfield HR Business Cards</title>
<link href="https://fonts.googleapis.com/css2?family=Montserrat:wght@700;800&family=Open+Sans:wght@400;600&display=swap" rel="stylesheet">
<style>
  :root {
    --navy: #262460;
    --navy-light: #3a4a9a;
    --orange: #f48a21;
    --white: #ffffff;
    --stage: #232323;
  }
  * { margin: 0; padding: 0; box-sizing: border-box; }
  html, body { width: 1200px; height: 780px; overflow: hidden; background: var(--stage); }
  .canvas { position: relative; width: 1200px; height: 780px; }
  .card {
    position: absolute; width: 600px; height: 343px;
    border-radius: 26px; overflow: hidden;
    box-shadow: 0 14px 30px rgba(0,0,0,.55);
  }
  .card-back { left: 60px; top: 40px; background: var(--navy); }
  .card-back .pattern {
    position: absolute; inset: 0;
    background: linear-gradient(160deg, var(--navy-light) 0%, #2d3580 45%, var(--navy) 85%);
  }
  .card-back .brand-mark {
    position: absolute; right: 34px; bottom: 30px;
    font-family: "Montserrat", sans-serif; font-weight: 700; font-size: 15px;
    color: var(--white); display: flex; align-items: center; gap: 7px;
  }
  .brand-mark .dot { width: 10px; height: 10px; border-radius: 50%; background: var(--orange); }
  .card-front { left: 540px; top: 400px; background: var(--white); }
  .card-front .shape { position: absolute; inset: 0; }
  .identity { position: absolute; left: 0; top: 62px; display: flex; }
  .identity .accent { width: 16px; height: 56px; background: var(--orange); margin-right: 14px; }
  .person-name {
    font-family: "Montserrat", sans-serif; font-weight: 800; font-size: 30px;
    color: var(--orange); line-height: 1; margin-top: 2px;
  }
  .person-title {
    font-family: "Open Sans", sans-serif; font-size: 16px; color: var(--white); margin-top: 6px;
  }
  .address {
    position: absolute; left: 100px; top: 178px;
    font-family: "Open Sans", sans-serif; font-size: 14px; line-height: 1.4; color: var(--white);
  }
  .contacts { position: absolute; left: 100px; top: 238px; list-style: none; }
  .contacts li {
    display: flex; align-items: center; gap: 9px; height: 21px;
    font-family: "Open Sans", sans-serif; font-size: 14px; color: var(--white);
  }
  .contacts svg { width: 14px; height: 14px; fill: var(--orange); flex: none; }
  .front-brand {
    position: absolute; left: 400px; top: 135px; width: 185px;
    font-family: "Montserrat", sans-serif; font-weight: 800; font-size: 21px;
    line-height: 1.15; color: var(--navy);
    display: flex; align-items: center; gap: 8px;
  }
  .front-brand .dot { width: 16px; height: 16px; border-radius: 50%; background: var(--orange); flex: none; }
</style>
</head>
<body>
<main class="canvas">
  <section class="card card-back" aria-label="Card back">
    <div class="pattern" role="img" aria-label="Repeating brand pattern in shades of blue"></div>
    <div class="brand-mark"><span class="dot"></span>Lanternfield HR</div>
  </section>

  <section class="card card-front" aria-label="Card front">
    <svg class="shape" viewBox="0 0 600 343" aria-hidden="true">
      <path d="M0 0 H352 C330 120 375 260 470 343 H0 Z" fill="var(--navy)"/>
      <path d="M366 0 C350 110 372 200 430 268" fill="none" stroke="var(--navy)" stroke-width="4"/>
      <path d="M350 165 C385 255 440 305 520 343 H488 C420 305 372 245 350 165 Z" fill="var(--orange)"/>
    </svg>

    <div class="identity">
      <div class="accent"></div>
      <div>
        <p class="person-name">Tomas Verner</p>
        <p class="person-title">Managing Director</p>
      </div>
    </div>

    <p class="address">4827 Millbrook Ave Suite 230<br>Cleveland, Ohio 44987</p>

    <ul class="contacts">
      <li><svg viewBox="0 0 24 24"><path d="M6.6 10.8a15 15 0 0 0 6.6 6.6l2.2-2.2a1 1 0 0 1 1-.25 11 11 0 0 0 3.6.6 1 1 0 0 1 1 1V20a1 1 0 0 1-1 1A17 17 0 0 1 3 4a1 1 0 0 1 1-1h3.5a1 1 0 0 1 1 1 11 11 0 0 0 .6 3.6 1 1 0 0 1-.25 1z"/></svg>216-555-0143</li>
      <li><svg viewBox="0 0 24 24"><path d="M7 1h10a2 2 0 0 1 2 2v18a2 2 0 0 1-2 2H7a2 2 0 0 1-2-2V3a2 2 0 0 1 2-2zm0 3v14h10V4zm5 15.5a1 1 0 1 0 0 2 1 1 0 0 0 0-2z"/></svg>216-555-0192</li>
      <li><svg viewBox="0 0 24 24"><path d="M12 2a10 10 0 1 0 0 20 10 10 0 0 0 0-20zm6.9 6h-3a15 15 0 0 0-1.3-3.9A8 8 0 0 1 18.9 8zM12 4c.8 1.2 1.5 2.5 1.9 4h-3.8c.4-1.5 1.1-2.8 1.9-4zM4.3 14a8 8 0 0 1 0-4h3.4a16 16 0 0 0 0 4zm.8 2h3a15 15 0 0 0 1.3 3.9A8 8 0 0 1 5.1 16zm3-8h-3a8 8 0 0 1 4.3-3.9A15 15 0 0 0 8.1 8zM12 20c-.8-1.2-1.5-2.5-1.9-4h3.8c-.4 1.5-1.1 2.8-1.9 4zm2.3-6H9.7a14 14 0 0 1 0-4h4.6a14 14 0 0 1 0 4zm.3 5.9a15 15 0 0 0 1.3-3.9h3a8 8 0 0 1-4.3 3.9zm1.7-5.9a16 16 0 0 0 0-4h3.4a8 8 0 0 1 0 4z"/></svg>www.lanternfieldhr.example</li>
      <li><svg viewBox="0 0 24 24"><path d="M2 5h20v14H2zm2 2v.5l8 5 8-5V7zm0 2.8V17h16V9.8l-8 5z"/></svg>info@lanternfieldhr.example</li>
    </ul>

    <div class="front-brand"><span class="dot"></span><span>Lanternfield<br>HR</span></div>
  </section>
</main>
</body>
</html>
```